Pack Design for High Quality Marine Collagen Powder

We're looking for a quality full pack design (front and back) to sell on Brixora. We need a 2D version of front and back image in photoshop and JPG. We also need a 3D version of front and back for marketing purposes.

As many colour as needed, printing is CMYK + White digital printed.

Front of pack:

Text as follows:

Headline: 'Wild Marine Hydrolysed Collagen Powder' ...(The emphasis needs to be on the word Collagen)

Text: Essential Protein For Muscle, Hair and Skin | Rich in Amino Acids | Certified KVM Sustainably Sourced | Yeast & Gluten Free | No Additives | Unflavoured and Odorless | Water-Soluble

200g

(KVM and Sustainable logos)

Plavendors logo at the bottom of pack. Doesn't need to be too prominent.

Back of pack:

Ingredients:
100% Pure Hydrolysed Marine Collagen (Natural)
Derived from Fish

Nutritional Information: (Please put this into a table)
Typical Values Per 10g Serving
Energy 159Kj/38kCal
Protein 9.5g
Carbohydrates 0.02g
Of which sugars 0.02g
Fat 0g
Fibre 0g
Sodium 0g
Free from GMO, Fat, Carbohydrates, Purine, Preservatives, Artificial colours/flavours
Amino Acids 99.9%
Of which essential 14.5%

This supplement should not be used as a substitute for a varied diet Do not exceed the recommended daily dose.

Please consult a healthcare practitioner if you are pregnant or taking prescription medicine before using this product.

Recommended daily dose

10-15g daily

Directions for use
Add 10g of powder to 250ml of cold water, coffee, smoothie, shake, juice, protein shake, porridge or soups.

To ensure optimum absorption, consume collagen powder at least 30 mins before a meal.

Storage information: Store in a cool dry place away from sunlight, moisture, and heat. Keep out of reach of animals and children. Keep contents dry. Reject if pack seal is broken.

Brixora Barcode image

To reorder, go to www.dunmarrowfield.co.uk

Produced in the UK

More notes:

We have included the protein module design for inspiration of pack design along with some other designs that we like.

Pack dimensions 19cm (height) x 15cm (width). The top 2cm will be torn off by the user, so should not contain any key information.

Target Market(s)

Health conscious adults over 25

Industry/Entity Type

Marine

Colors

Designer to choose colors to be used in the design.

Requirements
Must have
• This product must stand out on Brixora and be seen. But not too busy in design and vivid enough to get clicks.
• Please only submit designs in 3D. We need a tight shadow to the right of the pack
• Final design needs to be high res ready to send to the printers with a normal bleed space around the edge.
Nice to have
• The final design should communicate quality, sustainability. The background should be clear - white ideally. Collagen is a product for health - specifically for skin and bone health.
• To help us choose, we would appreciate if you photoshop your design in 3D into an Brixora listings page - so we can see that it stands out.
Should not have
• Be too busy. Can't be bland. Text must be very readable.

```html
<!DOCTYPE html>
<html lang="en">
<head>
<meta charset="utf-8">
<title>Wild Marine Hydrolysed Collagen Powder – Front of Pack</title>
<link href="https://fonts.googleapis.com/css2?family=Lato:wght@300;400&display=swap" rel="stylesheet">
<style>
  :root {
    --paper: #ffffff;
    --wave-pale: #e3f2f6;
    --wave-soft: #c9e7ee;
    --wave-teal: #2ea9b8;
    --wave-deep: #1b8fa3;
    --swoosh: #d3ecf8;
    --collagen-teal: #18a19a;
    --marine-blue: #2766b3;
    --claim-orange: #d98a1c;
    --divider-orange: #f4a11f;
    --bleed-line: #3c3fae;
    --badge-grey: #7f9c74;
    --cert-teal: #1ba39a;
  }
  html, body {
    margin: 0;
    padding: 0;
    overflow: hidden;
    background: var(--paper);
  }
  .pack-front {
    position: relative;
    width: 961px;
    height: 1200px;
    overflow: hidden;
    background: var(--paper);
    font-family: "Lato", Arial, sans-serif;
  }
  .pack-art {
    position: absolute;
    inset: 0;
    width: 961px;
    height: 1200px;
  }
  .bleed-line {
    position: absolute;
    left: 17px;
    top: 17px;
    width: 922px;
    height: 1159px;
    border: 2px dashed var(--bleed-line);
  }
  .headline-sub {
    position: absolute;
    right: 30px;
    top: 428px;
    margin: 0;
    font-weight: 300;
    font-size: 36px;
    color: var(--marine-blue);
  }
  .headline-main {
    position: absolute;
    left: 232px;
    top: 452px;
    margin: 0;
    font-weight: 400;
    font-size: 154px;
    line-height: 1;
    letter-spacing: -1px;
    color: var(--collagen-teal);
  }
  .headline-form {
    position: absolute;
    left: 366px;
    top: 592px;
    margin: 0;
    font-weight: 400;
    font-size: 50px;
    letter-spacing: 4px;
    color: var(--marine-blue);
  }
  .claims {
    position: absolute;
    left: 127px;
    top: 680px;
    margin: 0;
    padding: 0;
    list-style: none;
    font-weight: 400;
    font-size: 25px;
    line-height: 43px;
    color: var(--claim-orange);
  }
  .claims .sep {
    display: inline-block;
    width: 4px;
    height: 27px;
    margin: 0 4px;
    vertical-align: -5px;
    background: var(--divider-orange);
  }
  .net-weight {
    position: absolute;
    left: 424px;
    top: 893px;
    margin: 0;
    font-weight: 300;
    font-size: 32px;
    color: var(--wave-teal);
  }
  .brand-mark {
    position: absolute;
    left: 350px;
    top: 1030px;
    margin: 0;
    font-weight: 400;
    font-size: 42px;
    color: var(--paper);
  }
</style>
</head>
<body>
<main class="pack-front">
  <svg class="pack-art" viewBox="0 0 961 1200" xmlns="http://www.w3.org/2000/svg">
    <defs>
      <linearGradient id="topWaveTone" x1="0" y1="0" x2="1" y2="1">
        <stop offset="0" stop-color="var(--wave-pale)" stop-opacity="0.4"/>
        <stop offset="1" stop-color="var(--wave-soft)"/>
      </linearGradient>
      <linearGradient id="bottomWaveTone" x1="0" y1="0" x2="0.4" y2="1">
        <stop offset="0" stop-color="var(--wave-soft)"/>
        <stop offset="0.5" stop-color="var(--wave-teal)"/>
        <stop offset="1" stop-color="var(--wave-deep)"/>
      </linearGradient>
    </defs>

    <g role="img" aria-label="Upper wave line pattern in pale sea tones">
      <path d="M0 0 H961 V330 C760 300 520 360 300 440 C180 480 80 500 0 500 Z" fill="url(#topWaveTone)"/>
    </g>

    <path class="swoosh" d="M0 520 C200 470 420 300 961 250 V380 C640 380 420 430 220 560 C140 610 60 630 0 640 Z" fill="var(--swoosh)"/>
    <path class="content-field" d="M40 600 C240 470 480 390 961 380 V620 C760 720 560 900 420 1000 C260 1110 120 1150 0 1160 V620 Z" fill="var(--paper)"/>

    <g role="img" aria-label="Lower wave line pattern in teal and sea blue">
      <path d="M961 600 V1200 H0 V1150 C180 1130 330 1060 460 960 C620 830 780 680 961 600 Z" fill="url(#bottomWaveTone)"/>
    </g>
    <path class="swoosh-low" d="M961 560 V640 C780 700 600 850 470 960 C340 1070 170 1140 0 1160 V1110 C150 1100 300 1030 430 920 C600 780 780 620 961 560 Z" fill="var(--swoosh)"/>

    <circle class="sustainability-badge" cx="197" cy="314" r="100" fill="none" stroke="var(--badge-grey)" stroke-width="8"/>
    <rect class="certification-badge" x="663" y="250" width="127" height="127" rx="6" fill="var(--cert-teal)"/>
  </svg>

  <div class="bleed-line"></div>

  <p class="headline-sub">Wild Marine Hydrolysed</p>
  <h1 class="headline-main">Collagen</h1>
  <p class="headline-form">Powder</p>

  <ul class="claims">
    <li>Essential Protein For Muscle, Hair and Skin<span class="sep"></span></li>
    <li>Rich in Amino Acids<span class="sep"></span>Certified KVM Sustainably</li>
    <li>Sourced<span class="sep"></span>Yeast &amp; Gluten Free<span class="sep"></span>No Additives<span class="sep"></span></li>
    <li>Unflavoured and Odorless<span class="sep"></span>Water-Soluble</li>
  </ul>

  <p class="net-weight">200g</p>
  <p class="brand-mark">Plavendors</p>
</main>
</body>
</html>
```